Website redesign - valmoxy.com

We are looking to do a full redesign of valmoxy.com. Need a designer to come up overall layout and 3 specific pages and 3 different hero images.
Wireframes for the 3 pages are attached as well as site images. You don't have to follow the wireframes exactly, but instead the wireframe is there to show you the information that needs to be on each page. Feel free to rearrange as needed.
Our target market is self taught engineers. So definitely I want a more casual feel to it. I'm ok with fun bold colors as well. Really like websites that have the infinite scroll look/feel to them.
Looking to find a designer who will produce HTML and potentially even implement the HTML into our site checked in code.
HTML Code should be responsive/mobile first leveraging Bootstrap 4.
Attached files include:
0) Wireframe PDF
https://files.plimtree.net/share/8Kq2Lw7Zr4Tn9Vb3Xc6Md1Hs5Fy0Pj/view?ref=link
1) Valmoxy Images zip 1
https://files.plimtree.net/share/4Rt8Gm2Yk6Wd1Ne9Sb5Qh3Lx7Cv0Uz/view?ref=link
2) Valmoxy Images zip 2
https://files.plimtree.net/share/2Ja5Pf9Ko3Ex8Ti1Mr6Wg4Dn0Bs7Qy/view?ref=link
I sell DIY Waterproof Electronics enclosures. Target audience is self taught DIY engineers
Coded - Design and coding required
3 page
Designer to choose colors to be used in the design.

```html
<!DOCTYPE html>
<html lang="en">
<head>
<meta charset="utf-8">
<title>Valmoxy – Waterproof Project Boxes</title>
<link href="https://fonts.googleapis.com/css2?family=Barlow:wght@500;600;700&family=Lato:wght@400;700&display=swap" rel="stylesheet">
<style>
:root{
  --navy:#1d1b5c;
  --navy-deep:#17154a;
  --blue:#1a10d2;
  --lime:#b7c408;
  --lime-dark:#a4b005;
  --ink:#1e1e24;
  --muted:#55555f;
  --footer:#1b1b1d;
  --lav:#f5f4fb;
  --white:#fff;
}
*{box-sizing:border-box;margin:0;padding:0}
html,body{width:1200px;height:4800px;overflow:hidden}
body{position:relative;background:var(--white);font-family:'Lato',sans-serif;color:var(--ink)}
.abs{position:absolute}
.head-font{font-family:'Barlow',sans-serif}
.btn{position:absolute;display:flex;align-items:center;justify-content:center;font-family:'Barlow',sans-serif;font-weight:700;font-size:17px;text-transform:uppercase;color:var(--white);border-radius:3px;letter-spacing:.3px}
.btn-blue{background:var(--blue);box-shadow:0 4px 8px rgba(0,0,30,.25)}
.btn-lime{background:var(--lime)}
.photo{position:absolute}

/* header */
.site-header{position:absolute;left:0;top:0;width:1200px;height:97px;background:var(--white)}
.brand{position:absolute;display:flex;align-items:center;gap:8px;font-family:'Barlow',sans-serif;font-weight:700;color:var(--blue)}
.brand .dot{width:14px;height:14px;border-radius:50%;background:var(--lime)}
.site-header .brand{left:84px;top:18px;font-size:48px}
.main-nav{position:absolute;left:369px;top:38px;display:flex;gap:24px;font-family:'Barlow',sans-serif;font-weight:600;font-size:16px}
.main-nav a{color:var(--ink);text-decoration:none}
.main-nav a.active{color:var(--blue)}
.sign-in{left:903px;top:32px;width:103px;height:35px;font-size:16px}
.sign-up{left:1015px;top:32px;width:103px;height:35px;font-size:16px}

/* hero */
.hero{position:absolute;left:0;top:97px;width:1200px;height:630px;background:linear-gradient(180deg,var(--navy) 0%,var(--navy-deep) 100%);clip-path:polygon(0 0,1200px 0,1200px 518px,559px 630px,0 555px)}
.hero h1{position:absolute;left:110px;top:136px;width:400px;font-family:'Barlow',sans-serif;font-weight:600;font-size:41px;line-height:51px;color:var(--white)}
.hero .sub{position:absolute;left:110px;top:312px;font-size:24px;color:var(--white)}
.hero .btn{left:110px;top:369px;width:164px;height:41px}
.hero .photo{left:522px;top:52px;width:642px;height:475px;background:radial-gradient(ellipse at 50% 45%,#6a6a70 0%,#3c3a52 55%,rgba(29,27,92,0) 75%)}
.arrow{position:absolute;width:34px;height:34px;border-radius:50%;background:var(--lime);display:flex;align-items:center;justify-content:center}
.arrow svg{width:16px;height:16px}
.dot-indicator{position:absolute;left:303px;top:706px;width:16px;height:16px;border-radius:50%;border:1.5px solid #555}

/* designer */
.accent{position:absolute;background:var(--lime)}
.video{position:absolute;left:143px;top:820px;width:522px;height:311px;background:linear-gradient(135deg,#2a2a2a,#4a4d48 50%,#1b1b1b)}
.video .play{position:absolute;left:236px;top:130px;width:52px;height:52px;border-radius:50%;background:var(--lime);display:flex;align-items:center;justify-content:center}
.video .bar{position:absolute;left:0;bottom:0;width:100%;height:26px;background:rgba(0,0,0,.55)}
.designer-title{position:absolute;left:736px;top:896px;width:330px;font-family:'Barlow',sans-serif;font-weight:700;font-size:28px;line-height:37px;text-transform:uppercase}
.designer-btn{left:736px;top:1027px;width:164px;height:44px}

/* mounting kits */
.kits{position:absolute;left:0;top:1254px;width:1200px;height:699px;background:linear-gradient(180deg,var(--lime) 0%,var(--lime-dark) 100%)}
.kits h2{position:absolute;left:0;top:78px;width:1200px;text-align:center;font-family:'Barlow',sans-serif;font-weight:700;font-size:29px;line-height:40px;color:var(--white);text-transform:uppercase}
.kits .btn{left:518px;top:181px;width:164px;height:40px}
.kit-card{position:absolute;background:var(--white);box-shadow:0 6px 16px rgba(0,0,0,.12)}
.kit-card .photo{left:10%;top:14%;width:80%;height:72%;background:linear-gradient(160deg,#e6e6e3,#b8b8b4)}
.kit-left{left:138px;top:274px;width:237px;height:313px;clip-path:polygon(0 10px,237px 0,237px 313px,0 300px)}
.kit-center{left:393px;top:268px;width:412px;height:326px}
.kit-right{left:825px;top:274px;width:237px;height:313px;clip-path:polygon(0 0,237px 10px,237px 300px,0 313px)}
.arrow-blue{background:var(--blue);width:32px;height:32px}

/* makers */
.makers-title{position:absolute;left:143px;top:2062px;width:350px;font-family:'Barlow',sans-serif;font-weight:700;font-size:24px;line-height:33px;text-transform:uppercase}
.makers-rule{position:absolute;left:143px;top:2174px;width:62px;height:3px;background:var(--blue)}
.features{position:absolute;left:143px;top:2207px;width:330px;list-style:none;font-size:15.5px;line-height:21px;color:#333}
.features li{position:relative;padding-left:29px;margin-bottom:13px}
.features li::before{content:"";position:absolute;left:2px;top:3px;width:14px;height:14px;border-radius:50%;background:var(--lime)}
.makers-btn{left:143px;top:2398px;width:162px;height:40px}
.makers-photo{left:538px;top:2053px;width:516px;height:400px;background:linear-gradient(140deg,#6b5640,#9a7d5c 50%,#5e4c38)}

/* testimonials */
.reviews{position:absolute;left:0;top:2580px;width:1200px;height:582px;background:linear-gradient(180deg,var(--navy) 0%,var(--navy-deep) 100%);clip-path:polygon(0 0,1200px 0,1200px 494px,316px 582px,0 475px)}
.reviews h2{position:absolute;left:0;top:83px;width:1200px;text-align:center;font-family:'Barlow',sans-serif;font-weight:700;font-size:31px;color:var(--white);text-transform:uppercase}
.reviews .rule{position:absolute;left:559px;top:150px;width:80px;height:3px;background:var(--white)}
.review{position:absolute;top:215px;width:432px;height:167px;background:var(--white)}
.review::after{content:"";position:absolute;left:70px;bottom:-22px;border-left:0 solid transparent;border-right:38px solid transparent;border-top:22px solid var(--white)}
.review .avatar{position:absolute;left:18px;top:20px;width:106px;height:106px;border-radius:50%;background:linear-gradient(160deg,#d6d8dc,#7c8696);border:4px solid #eceef2}
.review p{position:absolute;left:146px;top:30px;width:258px;font-size:14.5px;line-height:24px;color:#555}
.review .quote{position:absolute;right:16px;bottom:-18px;font-family:'Barlow',sans-serif;font-weight:700;font-size:80px;color:var(--lime);line-height:1}
.review-name{position:absolute;top:400px;font-size:19px;font-style:italic;color:var(--white)}
.stars{position:absolute;top:427px;font-size:16px;letter-spacing:2px;color:var(--lime)}

/* examples */
.examples{position:absolute;left:0;top:3162px;width:1200px;height:1300px;background:var(--lav)}
.examples h2{position:absolute;left:0;top:75px;width:1200px;text-align:center;font-family:'Barlow',sans-serif;font-weight:600;font-size:32px;text-transform:uppercase}
.examples .rule{position:absolute;left:559px;top:133px;width:80px;height:3px;background:var(--lime)}
.example{position:absolute;width:282px;height:302px;background:var(--white);box-shadow:0 4px 10px rgba(0,0,0,.1)}
.example .photo{left:8px;top:8px;width:266px;height:212px;background:linear-gradient(150deg,#f2f2f2,#c9c9cb 60%,#e8e8ea)}
.example .caption{position:absolute;left:0;top:240px;width:100%;text-align:center;font-family:'Barlow',sans-serif;font-weight:500;font-size:17px;line-height:22px;color:#333}

/* footer */
.site-footer{position:absolute;left:0;top:4430px;width:1200px;height:370px}
.site-footer svg.shape{position:absolute;left:0;top:0}
.site-footer .brand{left:0;top:88px;width:1200px;justify-content:center;font-size:48px}
.contact-row{position:absolute;left:0;top:144px;width:1200px;display:flex;justify-content:center;gap:44px;font-size:16px;color:#ddd}
.contact-row span{display:flex;align-items:center;gap:10px}
.contact-row svg{width:13px;height:13px;fill:#ddd}
.footer-links{position:absolute;left:0;top:191px;width:1200px;text-align:center;font-size:16px;color:#ddd}
.copyright{position:absolute;left:0;top:238px;width:1200px;text-align:center;font-size:16px;color:#ddd}
.socials{position:absolute;left:0;top:284px;width:1200px;display:flex;justify-content:center;gap:14px}
.socials span{width:40px;height:40px;border-radius:50%;border:1.5px solid #ccc;display:block}
</style>
</head>
<body>

<header class="site-header">
  <div class="brand"><span class="dot"></span>Valmoxy</div>
  <nav class="main-nav">
    <a class="active">HOME</a><a>GET STARTED</a><a>DESIGNS</a><a>FAQS</a><a>VIDEOS</a><a>CONTACT</a>
  </nav>
  <div class="btn btn-blue sign-in">Sign In</div>
  <div class="btn btn-lime sign-up">Sign Up</div>
</header>

<section class="hero">
  <h1>Waterproof Project Boxes Customized to your Exact Needs</h1>
  <div class="sub">(at a fraction of the price)</div>
  <div class="btn btn-lime">Get Started</div>
  <div class="photo" role="img" aria-label="Assembled project box mounting plate with controller boards and wiring"></div>
  <div class="arrow" style="left:43px;top:242px"><svg viewBox="0 0 16 16"><path d="M8 3 3 8l5 5M13 3 8 8l5 5" fill="none" stroke="#fff" stroke-width="2"/></svg></div>
  <div class="arrow" style="left:1121px;top:242px"><svg viewBox="0 0 16 16"><path d="m8 3 5 5-5 5M3 3l5 5-5 5" fill="none" stroke="#fff" stroke-width="2"/></svg></div>
</section>
<div class="dot-indicator"></div>

<section class="designer">
  <div class="accent" style="left:615px;top:802px;width:72px;height:68px"></div>
  <div class="accent" style="left:125px;top:1086px;width:70px;height:69px"></div>
  <div class="video" role="img" aria-label="Video still of a power supply and controller inside an enclosure">
    <div class="play"><svg width="20" height="22" viewBox="0 0 20 22"><path d="M2 1l17 10L2 21z" fill="#fff"/></svg></div>
    <div class="bar"></div>
  </div>
  <h2 class="designer-title">Customize your project box using our designer</h2>
  <div class="btn btn-blue designer-btn">Get Started</div>
</section>

<section class="kits">
  <h2>Mounting kits for all the popular water proof project<br>boxes with many sizes to choose from</h2>
  <div class="btn btn-blue">Get Started</div>
  <div class="kit-card kit-left"><div class="photo" role="img" aria-label="Grey waterproof enclosure"></div></div>
  <div class="kit-card kit-center"><div class="photo" role="img" aria-label="Large grey waterproof enclosure with latches"></div></div>
  <div class="kit-card kit-right"><div class="photo" role="img" aria-label="Grey waterproof enclosure"></div></div>
  <div class="arrow arrow-blue" style="left:386px;top:424px"><svg viewBox="0 0 16 16"><path d="M8 3 3 8l5 5M13 3 8 8l5 5" fill="none" stroke="#fff" stroke-width="2"/></svg></div>
  <div class="arrow arrow-blue" style="left:779px;top:424px"><svg viewBox="0 0 16 16"><path d="m8 3 5 5-5 5M3 3l5 5-5 5" fill="none" stroke="#fff" stroke-width="2"/></svg></div>
</section>

<section class="makers">
  <h2 class="makers-title">Valmoxy waterproof project boxes were built by makers for makers</h2>
  <div class="makers-rule"></div>
  <ul class="features">
    <li>Design to your specifications</li>
    <li>Maker components: Ardello, Bramble Pi, Voltwell Power</li>
    <li>Detailed build instructions, videos, walkthroughs</li>
    <li>DIY made to look professional</li>
  </ul>
  <div class="btn btn-blue makers-btn">Get Started</div>
  <div class="accent" style="left:997px;top:2042px;width:69px;height:69px"></div>
  <div class="accent" style="left:529px;top:2399px;width:69px;height:68px"></div>
  <div class="photo makers-photo" role="img" aria-label="Unassembled mounting kit with boards, power supply and hardware on a table"></div>
</section>

<section class="reviews">
  <h2>What our customers have to say</h2>
  <div class="rule"></div>
  <div class="review" style="left:153px">
    <div class="avatar" role="img" aria-label="Customer portrait"></div>
    <p>Great work at a reasonable cost. I can't recommend them enough. If you're doing custom boxes for light shows, this is where you go.</p>
    <div class="quote">”</div>
  </div>
  <div class="review" style="left:617px">
    <div class="avatar" role="img" aria-label="Customer portrait"></div>
    <p>Fantastic service/product.. whether you simply generate the design and do all of the fabrication yourself or simply order the kits.</p>
    <div class="quote">”</div>
  </div>
  <div class="review-name" style="left:225px">-Marcus T</div>
  <div class="stars" style="left:225px">★★★★★</div>
  <div class="review-name" style="left:689px">-Dylan R.</div>
  <div class="stars" style="left:689px">★★★★★</div>
  <div class="arrow" style="left:74px;top:285px"><svg viewBox="0 0 16 16"><path d="M8 3 3 8l5 5M13 3 8 8l5 5" fill="none" stroke="#fff" stroke-width="2"/></svg></div>
  <div class="arrow" style="left:1091px;top:285px"><svg viewBox="0 0 16 16"><path d="m8 3 5 5-5 5M3 3l5 5-5 5" fill="none" stroke="#fff" stroke-width="2"/></svg></div>
</section>

<section class="examples">
  <h2>See real examples from our customers</h2>
  <div class="rule"></div>
  <div class="example" style="left:143px;top:188px"><div class="photo" role="img" aria-label="Customer build with controller boards on standoffs" style="background:linear-gradient(150deg,#fbfbe6,#d7d8c8)"></div><div class="caption">+ KTR BX8-72 w/ G16v3<br>Expansion board</div></div>
  <div class="example" style="left:466px;top:188px"><div class="photo" role="img" aria-label="Customer build with controller boards on standoffs"></div><div class="caption">+ KTR BX8-72 w/ G16v3<br>Expansion board</div></div>
  <div class="example" style="left:773px;top:188px"><div class="photo" role="img" aria-label="Customer build with controller boards on standoffs"></div><div class="caption">+ KTR BX8-72 w/ G16v3<br>Expansion board</div></div>
  <div class="example" style="left:143px;top:523px"><div class="photo" role="img" aria-label="Customer build with power supply on mounting plate"></div><div class="caption">+ KTR BX8-72 w/ G16v3<br>Expansion board</div></div>
  <div class="example" style="left:466px;top:523px"><div class="photo" role="img" aria-label="Customer build with power supply on mounting plate"></div><div class="caption">+ KTR BX8-72 w/ G16v3<br>Expansion board</div></div>
  <div class="example" style="left:773px;top:523px"><div class="photo" role="img" aria-label="Customer build with power supplies and wiring"></div><div class="caption">+ KTR BX8-72 w/ G16v3<br>Expansion board</div></div>
  <div class="example" style="left:143px;top:858px"><div class="photo" role="img" aria-label="Customer build with wired controller board"></div><div class="caption">+ KTR BX8-72 w/ G16v3<br>Expansion board</div></div>
  <div class="example" style="left:466px;top:858px"><div class="photo" role="img" aria-label="Customer build on dark mounting plate"></div><div class="caption">+ KTR BX8-72 w/ G16v3<br>Expansion board</div></div>
  <div class="example" style="left:773px;top:858px"><div class="photo" role="img" aria-label="Customer build with stacked plates"></div><div class="caption">+ KTR BX8-72 w/ G16v3<br>Expansion board</div></div>
</section>

<footer class="site-footer">
  <svg class="shape" width="1200" height="370" viewBox="0 0 1200 370">
    <polygon points="0,78 600,0 1200,78 1200,370 0,370" fill="var(--footer)"/>
    <polyline points="0,78 600,0 1200,78" fill="none" stroke="var(--blue)" stroke-width="6"/>
  </svg>
  <div class="brand"><span class="dot"></span>Valmoxy</div>
  <div class="contact-row">
    <span><svg viewBox="0 0 12 16"><path d="M6 0a6 6 0 0 0-6 6c0 4.5 6 10 6 10s6-5.5 6-10a6 6 0 0 0-6-6zm0 8.5A2.5 2.5 0 1 1 6 3.5a2.5 2.5 0 0 1 0 5z"/></svg>Valmoxy, enim ipsam, 6018</span>
    <span><svg viewBox="0 0 16 16"><path d="M3.6 1 6 4.2 4.6 6a9 9 0 0 0 5.4 5.4L11.8 10 15 12.4 13.4 15C6.8 14.6 1.4 9.2 1 2.6z"/></svg>808-555-0147</span>
    <span><svg viewBox="0 0 16 12"><path d="M0 0h16v12H0zM1.5 1.5 8 6.5l6.5-5" /></svg>info@valmoxy.com</span>
  </div>
  <div class="footer-links">Get Started &nbsp;|&nbsp; Designs &nbsp;|&nbsp; FAQs &nbsp;|&nbsp; Videos &nbsp;|&nbsp; Contact</div>
  <div class="copyright">© 2019 Valmoxy. All Rights Reserved.</div>
  <div class="socials"><span></span><span></span><span></span></div>
</footer>

</body>
</html>
```